Car finance company business card

Create a nice business card for our car financing company , Visit our website www.birchlanefinance.com for the phone number and idea of the company look. Please do not be afraid to be creative. Name on card Is Marc-Antoine Beaulieu and phone number is on our website adress of business is
27816 Boulevard Saint-Orvel,
Mirabel, QC K4R 2T8

```html
<!DOCTYPE html>
<html lang="fr">
<head>
<meta charset="utf-8">
<title>Birch Lane Finance – Business Card</title>
<link href="https://fonts.googleapis.com/css2?family=Arimo:wght@400&family=Montserrat:wght@700;800&family=Roboto:wght@400;500&display=swap" rel="stylesheet">
<style>
  :root {
    --page-bg: #e9e5df;
    --card-white: #ffffff;
    --brand-blue: #1b80c4;
    --ink: #1f1f1f;
    --ink-soft: #2b2b2b;
    --accent-orange: #f26b21;
    --mascot-orange: #f0792b;
    --mascot-purple: #5a4bb0;
    --stripe-black: #111111;
  }
  * { margin: 0; padding: 0; box-sizing: border-box; }
  html, body { width: 900px; height: 1200px; overflow: hidden; }
  body {
    background: var(--page-bg);
    position: relative;
    font-family: "Roboto", Arial, sans-serif;
  }
  .card {
    position: absolute;
    left: 82px;
    width: 738px;
    height: 432px;
    border-radius: 44px 8px 44px 8px;
    overflow: hidden;
    box-shadow: 0 6px 14px rgba(0,0,0,0.35);
  }
  /* Front */
  .card-front { top: 124px; background: linear-gradient(160deg, #ffffff 40%, #eeeeee 100%); }
  .brand-name {
    position: absolute;
    left: 175px; top: 130px;
    width: 245px;
    font-family: "Montserrat", Arial, sans-serif;
    font-weight: 800;
    font-size: 31px;
    line-height: 40px;
    color: var(--ink);
    text-transform: uppercase;
    white-space: nowrap;
    z-index: 1;
  }
  .mascot-front {
    position: absolute;
    left: 428px; top: 58px;
    width: 142px; height: 200px;
    border-radius: 40px;
    background: linear-gradient(180deg, var(--mascot-orange) 0%, #e8672a 55%, var(--mascot-purple) 100%);
  }
  .contact-block {
    position: absolute;
    top: 313px;
    font-size: 16px;
    line-height: 23px;
    color: var(--ink-soft);
    white-space: nowrap;
  }
  .contact-person { left: 38px; }
  .contact-address { left: 248px; padding-left: 15px; border-left: 1.5px solid var(--ink); }
  .contact-reach { left: 503px; padding-left: 13px; border-left: 1.5px solid var(--ink); }
  .person-name { font-weight: 500; font-size: 18px; color: var(--ink); }
  .person-title { color: var(--brand-blue); }
  .band-black {
    position: absolute; left: 0; bottom: 20px; width: 100%; height: 10px;
    background: var(--stripe-black);
  }
  .band-blue {
    position: absolute; left: 0; bottom: 0; width: 100%; height: 20px;
    background: var(--brand-blue);
  }
  .url-tab {
    position: absolute; right: 0; bottom: 0;
    width: 262px; height: 32px;
    background: var(--brand-blue);
    border-top-left-radius: 22px;
    color: #fff;
    font-size: 15px;
    line-height: 32px;
    padding-left: 34px;
  }
  /* Back */
  .card-back { top: 640px; background: var(--brand-blue); }
  .headline {
    position: absolute; left: 58px; top: 46px;
    font-family: "Montserrat", Arial, sans-serif;
    font-weight: 700;
    font-size: 25px;
    line-height: 32.5px;
    color: #fff;
    text-transform: uppercase;
  }
  .criteria {
    position: absolute; left: 58px; top: 159px;
    list-style: none;
    color: #fff;
    font-family: "Arimo", Arial, sans-serif;
    font-size: 18px;
    line-height: 28.7px;
  }
  .criteria li { display: flex; align-items: center; }
  .tick { width: 16px; height: 14px; margin-right: 4px; flex: none; }
  .mascot-back {
    position: absolute; left: 392px; top: 12px;
    width: 336px; height: 412px;
    border-radius: 80px;
    background: linear-gradient(180deg, var(--mascot-orange) 0%, #ea6b28 50%, var(--mascot-purple) 100%);
  }
</style>
</head>
<body>
  <section class="card card-front">
    <div class="brand-name">Birch Lane<br>Finance</div>
    <div class="mascot-front" role="img" aria-label="Cartoon fox mascot in a suit giving a thumbs up and holding car keys"></div>
    <div class="contact-block contact-person">
      <div class="person-name">Marc-Antoine Beaulieu</div>
      <div class="person-title">Managing director</div>
    </div>
    <div class="contact-block contact-address">
      <div>27816 Boulevard Saint-Orvel</div>
      <div>Mirabel, QC K4R 2T8</div>
    </div>
    <div class="contact-block contact-reach">
      <div>(514) 555-0187</div>
      <div>marc@birchlanefinance.com</div>
    </div>
    <div class="band-black"></div>
    <div class="band-blue"></div>
    <div class="url-tab">www.birchlanefinance.com</div>
  </section>

  <section class="card card-back">
    <h1 class="headline">1re, 2e, 3e<br>chance au crédit<br>aucun cas refusé</h1>
    <svg width="0" height="0" style="position:absolute">
      <symbol id="tick" viewBox="0 0 16 14"><path d="M1.5 7.5 L6 12 L14.5 1.5" fill="none" stroke="#f26b21" stroke-width="3" stroke-linecap="round" stroke-linejoin="round"/></symbol>
    </svg>
    <ul class="criteria">
      <li><svg class="tick"><use href="#tick"/></svg>Proposition au consommateur</li>
      <li><svg class="tick"><use href="#tick"/></svg>Remise volontaire</li>
      <li><svg class="tick"><use href="#tick"/></svg>Retards de paiements</li>
      <li><svg class="tick"><use href="#tick"/></svg>Recouvrements</li>
      <li><svg class="tick"><use href="#tick"/></svg>Faible revenu</li>
      <li><svg class="tick"><use href="#tick"/></svg>Récemment travailleur autonome</li>
      <li><svg class="tick"><use href="#tick"/></svg>Faillite</li>
      <li><svg class="tick"><use href="#tick"/></svg>mauvais crédit</li>
    </ul>
    <div class="mascot-back" role="img" aria-label="Large cartoon fox mascot in a purple suit giving a thumbs up with car keys"></div>
  </section>
</body>
</html>
```